Lanterne architecture business cards

We are a new company based in New Zealand. We Specialize in High end Luxury Residential Architecture.

Every home is bespoke and is designed to each clients individual requirements and needs.

I like to design buildings that inspire people through light and form while offering a high level of comfort and usability.

Lines of sight, proportion and balance are fundamental to the spaces I create.
Updates

August 5th is current deadline - Today's date is the 13th of August.

Target Market(s)

New Zealanders who want a custom individual home design, typically 30-65 year old males and females

Industry/Entity Type

Architecture

Contact Information for Business Card

Director - Derek Tolson
Contact Number - 0279164073
Email - info@lanternearchitecture-example.co.nz
Webstie - www.lanternearchitecture-example.co.nz
Social Media - @lanternearchitecture

Font styles to use
Sans Serif

Requirements
Must have
• Logo (Both Sides)
Website
Email
Contact Number
Social Media

Nice to have
• Texture
Should not have
• More than 3 colours - typically I would've thought 2 would be good to match the logo.

```html
<!DOCTYPE html>
<html lang="en">
<head>
<meta charset="utf-8">
<title>Lanterne architecture – business cards</title>
<link rel="stylesheet" href="https://fonts.googleapis.com/css2?family=Lato:wght@400;700&display=swap">
<style>
  :root {
    --backdrop: #3a322e;
    --card: #0b0b0b;
    --ink: #ffffff;
    --ink-soft: #d9d9d9;
  }
  * { box-sizing: border-box; margin: 0; padding: 0; }
  html, body {
    width: 1200px; height: 847px; overflow: hidden;
    background: var(--backdrop);
    font-family: "Lato", sans-serif;
    color: var(--ink);
  }
  .canvas {
    width: 1200px; height: 847px;
    display: flex; align-items: center; justify-content: center; gap: 40px;
  }
  .card {
    width: 540px; height: 309px;
    background: var(--card);
    position: relative;
    box-shadow: 0 10px 30px rgba(0,0,0,.45);
  }
  .brand {
    display: flex; flex-direction: column; align-items: center; gap: 14px;
  }
  .brand-dot {
    width: 34px; height: 34px; border-radius: 50%;
    border: 3px solid var(--ink);
  }
  .brand-name {
    font-weight: 400; font-size: 15px; letter-spacing: 6px;
    text-transform: uppercase; white-space: nowrap; color: var(--ink);
  }
  .card--front { display: flex; align-items: center; justify-content: center; }
  .card--front .brand-dot { width: 44px; height: 44px; }
  .card--front .brand-name { font-size: 18px; letter-spacing: 8px; }

  .card--back .brand {
    position: absolute; left: 30px; top: 92px; width: 230px;
  }
  .card--back .brand-name { font-size: 11px; letter-spacing: 4px; }
  .divider {
    position: absolute; left: 275px; top: 82px;
    width: 1px; height: 112px; background: var(--ink-soft);
  }
  .contact { position: absolute; left: 295px; top: 96px; }
  .contact-name { font-weight: 700; font-size: 22px; line-height: 1.1; }
  .contact-role { font-size: 12px; color: var(--ink-soft); margin: 2px 0 12px; }
  .contact-list { list-style: none; font-size: 11.5px; line-height: 1; }
  .contact-list li { display: flex; align-items: center; gap: 8px; margin-bottom: 6px; }
  .contact-list svg { width: 11px; height: 11px; flex: none; }
  .social {
    position: absolute; left: 70px; top: 228px;
    display: flex; align-items: center; gap: 8px; font-size: 14px;
  }
  .social-dot { width: 11px; height: 11px; background: var(--ink); border-radius: 2px; }
</style>
</head>
<body>
<main class="canvas">
  <section class="card card--front" aria-label="Card front">
    <div class="brand">
      <span class="brand-dot"></span>
      <span class="brand-name">Lanterne architecture</span>
    </div>
  </section>

  <section class="card card--back" aria-label="Card back">
    <div class="brand">
      <span class="brand-dot"></span>
      <span class="brand-name">Lanterne architecture</span>
    </div>
    <span class="divider"></span>
    <div class="contact">
      <p class="contact-name">Derek Tolson</p>
      <p class="contact-role">Director</p>
      <ul class="contact-list">
        <li>
          <svg viewBox="0 0 12 12" aria-hidden="true"><path d="M3 1 L5 3.5 L4 5 Q5 7 7 8 L8.5 7 L11 9 L9.5 11 Q5 11 1 6 Q1 2.5 3 1 Z" fill="none" stroke="#fff" stroke-width="1.1"/></svg>
          0279164073
        </li>
        <li>
          <svg viewBox="0 0 12 12" aria-hidden="true"><rect x="0.8" y="2.3" width="10.4" height="7.4" fill="none" stroke="#fff" stroke-width="1.1"/><path d="M1 2.6 L6 6.6 L11 2.6" fill="none" stroke="#fff" stroke-width="1.1"/></svg>
          info@lanternearchitecture-example.co.nz
        </li>
        <li>
          <svg viewBox="0 0 12 12" aria-hidden="true"><circle cx="6" cy="6" r="5" fill="none" stroke="#fff" stroke-width="1.1"/><ellipse cx="6" cy="6" rx="2.2" ry="5" fill="none" stroke="#fff" stroke-width="0.9"/><path d="M1 6 H11" stroke="#fff" stroke-width="0.9"/></svg>
          www.lanternearchitecture-example.co.nz
        </li>
      </ul>
    </div>
    <div class="social">
      <span class="social-dot"></span>
      <span>@lanternearchitecture</span>
    </div>
  </section>
</main>
</body>
</html>
```